New modern business card design

To design a brand new business card that's clean & modern in terms of layout.
I have attached our company logo and also basic information regarding what is needed on the card that also needs to be editable.

Target Market(s)

motor trade

Contact Information for Business Card

logo, name, title, tel, mob, email, address, www, all information is in the word.doc file

Requirements
Must have
• white background
Nice to have
• Nice clean font

```html
<!DOCTYPE html>
<html lang="en">
<head>
<meta charset="utf-8">
<title>Northfield Extract Ltd – Business Card</title>
<link href="https://fonts.googleapis.com/css2?family=Montserrat:wght@400;500&display=swap" rel="stylesheet">
<style>
  :root {
    --backdrop: #2b2b2b;
    --card: #ffffff;
    --brand-blue: #1a78c9;
    --brand-grey: #9a9a9a;
    --text-grey: #666666;
  }
  * { box-sizing: border-box; margin: 0; padding: 0; }
  html, body { width: 1200px; height: 930px; overflow: hidden; }
  body {
    background: var(--backdrop);
    font-family: "Montserrat", sans-serif;
    position: relative;
  }
  .card {
    position: absolute;
    width: 560px;
    height: 320px;
    background: var(--card);
    box-shadow: 0 12px 30px rgba(0,0,0,0.45);
    overflow: hidden;
  }
  .card--front { left: 90px; top: 90px; }
  .card--back { left: 550px; top: 500px; }

  .brand {
    display: flex;
    align-items: center;
    gap: 12px;
    color: var(--brand-blue);
    font-weight: 500;
    letter-spacing: 0.06em;
    text-transform: uppercase;
    white-space: nowrap;
  }
  .brand__square { width: 22px; height: 22px; background: var(--brand-blue); }
  .brand__rule { height: 1.5px; background: var(--brand-blue); margin-top: 10px; }

  .card--front .brand-block {
    position: absolute; left: 50%; top: 50%;
    transform: translate(-50%, -50%);
  }
  .card--front .brand { font-size: 26px; }

  .card--back .brand-block { position: absolute; right: 34px; top: 30px; }
  .card--back .brand { font-size: 18px; }
  .card--back .brand__square { width: 16px; height: 16px; }

  .details {
    position: absolute; left: 0; top: 100px; right: 0;
  }
  .person {
    position: relative; padding-left: 38px;
  }
  .person__accent {
    position: absolute; left: 0; top: 3px; width: 16px; height: 38px;
    background: var(--brand-blue);
  }
  .person__accent::after {
    content: ""; position: absolute; left: 21px; top: 0; width: 3px; height: 38px;
    background: var(--brand-grey);
  }
  .person__name {
    color: var(--brand-blue); font-size: 21px; font-weight: 500; line-height: 1.2;
    letter-spacing: 0.03em; text-transform: uppercase;
  }
  .person__title { color: var(--text-grey); font-size: 12.5px; line-height: 1.3; margin-top: 1px; }
  .address {
    font-style: normal; color: var(--text-grey); font-size: 12px;
    line-height: 1.4; margin-top: 16px; margin-left: 38px;
  }
  .contact { list-style: none; margin-top: 12px; margin-left: 56px; }
  .contact li {
    display: flex; align-items: center; gap: 10px;
    color: var(--text-grey); font-size: 12px; line-height: 1.45;
  }
  .contact svg { width: 11px; height: 11px; flex: none; }
  .contact .domain { color: var(--brand-blue); }
</style>
</head>
<body>

<section class="card card--front" aria-label="Business card front">
  <div class="brand-block">
    <div class="brand"><span class="brand__square"></span>Northfield Extract Ltd</div>
    <div class="brand__rule"></div>
  </div>
</section>

<section class="card card--back" aria-label="Business card back">
  <div class="brand-block">
    <div class="brand"><span class="brand__square"></span>Northfield Extract Ltd</div>
    <div class="brand__rule"></div>
  </div>

  <div class="details">
    <div class="person">
      <span class="person__accent"></span>
      <h1 class="person__name">Daniel Hargreave</h1>
      <p class="person__title">General Manager</p>
    </div>

    <address class="address">
      Kestrel Lane<br>
      Denby Vale, Northbridge<br>
      NB4 2QT
    </address>

    <ul class="contact">
      <li>
        <svg viewBox="0 0 12 12" aria-hidden="true"><path d="M3 1 L5 3.5 L4 5 Q5 7 7 8 L8.5 7 L11 9 L9.5 11 Q5 11 1 5 Q1 2 3 1Z" fill="var(--brand-blue)"/></svg>
        0123 456 7890
      </li>
      <li>
        <svg viewBox="0 0 12 12" aria-hidden="true"><rect x="3" y="0.8" width="6" height="10.4" rx="1" fill="none" stroke="var(--brand-blue)" stroke-width="1.2"/><circle cx="6" cy="9.3" r="0.6" fill="var(--brand-blue)"/></svg>
        07000 123 456
      </li>
      <li>
        <svg viewBox="0 0 12 12" aria-hidden="true"><rect x="0.8" y="2.5" width="10.4" height="7" fill="none" stroke="var(--brand-blue)" stroke-width="1.2"/><path d="M1 3 L6 7 L11 3" fill="none" stroke="var(--brand-blue)" stroke-width="1.2"/></svg>
        dhargreave@northfield-extract.co.uk
      </li>
      <li>
        <svg viewBox="0 0 12 12" aria-hidden="true"><circle cx="6" cy="6" r="5" fill="none" stroke="var(--brand-blue)" stroke-width="1.1"/><ellipse cx="6" cy="6" rx="2.2" ry="5" fill="none" stroke="var(--brand-blue)" stroke-width="1"/><path d="M1 6 H11" stroke="var(--brand-blue)" stroke-width="1"/></svg>
        <span>www.<span class="domain">northfield-extract</span>.co.uk</span>
      </li>
    </ul>
  </div>
</section>

</body>
</html>
```